***Flyer*** TORNILEX AUTO TRANSPORT *** Flyer***

I need a flyer design that explain my auto transport business... the design must be eye catching and draws a persons attention at first site. We Tow Cars locally in the City of Houston for a flat rate of $75... We ask that the designer make the $75 standout so it will catch the attention of the reader. Much of the content writing can be gather from my website tornilexautotransport.com - the designer can use his own images to express his design work... I will attach the logo and some samples of some reason business and post cards designs. If you chose you can also add these images in your designs if it will help.

Size of flyer is 8"x11" front and back

Automotive

Requirements
Must have
• $75 or $75.00
• (281) 555-0137
• service@tornilexautotransport.com
• www.tornilexautotransport.com
Nice to have
• WE REALLY WANT TO EARN YOUR BUSINESS
• Note: Please look at my website for content writing to create your flyer.

```html
<!DOCTYPE html>
<html lang="en">
<head>
<meta charset="utf-8">
<title>Tornilex Auto Transport – Flyer</title>
<link href="https://fonts.googleapis.com/css2?family=Inter:wght@300;400&display=swap" rel="stylesheet">
<style>
  :root{
    --red:#c8141c;
    --red-deep:#8e0d12;
    --orange:#e8561a;
    --maroon:#3a0a0c;
    --white:#ffffff;
  }
  html,body{margin:0;padding:0;overflow:hidden;background:#fff;}
  .flyer{
    position:relative;width:879px;height:1200px;overflow:hidden;
    background:#fff;font-family:'Inter',Helvetica,Arial,sans-serif;color:var(--white);
  }
  .hero-photo{
    position:absolute;left:11px;top:11px;width:858px;height:1180px;
    background:
      radial-gradient(ellipse 420px 300px at 380px 420px, rgba(240,120,30,.75), rgba(240,120,30,0) 70%),
      radial-gradient(ellipse 500px 260px at 620px 860px, rgba(235,110,25,.7), rgba(235,110,25,0) 70%),
      linear-gradient(100deg, #e2331a 0%, #b8161a 40%, #6c0e12 75%, var(--maroon) 100%);
  }
  .top-rule{position:absolute;left:11px;top:11px;width:858px;height:2px;background:var(--white);opacity:.9;}
  .brand-box{
    position:absolute;left:4px;top:24px;width:235px;height:85px;
    background:linear-gradient(180deg,var(--red),var(--red-deep));
    border:1px solid rgba(255,255,255,.8);box-sizing:border-box;
    display:flex;flex-direction:column;align-items:center;justify-content:center;
  }
  .brand-name{font-weight:400;font-size:20px;letter-spacing:1px;line-height:1.2;text-align:center;}
  .title-box{
    position:absolute;left:250px;top:24px;width:619px;height:85px;
    border:1px solid rgba(255,255,255,.85);box-sizing:border-box;
    background:rgba(180,14,20,.55);
  }
  .title{
    position:absolute;left:19px;top:20px;margin:0;
    font-weight:300;font-size:42px;letter-spacing:-1px;line-height:1;white-space:nowrap;
  }
  .intro{
    position:absolute;left:270px;top:128px;margin:0;
    font-weight:300;font-size:31px;line-height:41px;letter-spacing:-.5px;
  }
  .website{
    position:absolute;left:225px;top:357px;
    transform:translate(-50%,-50%) rotate(-90deg);
    white-space:nowrap;font-weight:300;font-size:30px;letter-spacing:-.5px;
  }
  .phone{
    position:absolute;left:461px;top:533px;margin:0;
    font-weight:300;font-size:50px;letter-spacing:-1px;line-height:1;white-space:nowrap;
  }
  .rate{
    position:absolute;left:470px;top:850px;margin:0;text-align:left;line-height:1;
  }
  .rate-label{display:block;font-weight:300;font-size:30px;letter-spacing:3px;}
  .rate-price{display:block;font-weight:400;font-size:150px;letter-spacing:-4px;margin-top:4px;}
  .email{
    position:absolute;left:270px;top:1113px;margin:0;
    font-weight:300;font-size:31px;letter-spacing:-.5px;line-height:1;white-space:nowrap;
  }
  .guides{position:absolute;left:0;top:0;width:879px;height:1200px;pointer-events:none;}
</style>
</head>
<body>
<div class="flyer">
  <div class="hero-photo" role="img" aria-label="Photo of an SUV being loaded onto a red flatbed tow truck ramp at dusk, tinted red and orange"></div>
  <div class="top-rule"></div>

  <div class="brand-box">
    <div class="brand-name">TORNILEX<br>AUTO TRANSPORT</div>
  </div>

  <div class="title-box"><h1 class="title">TOWING MADE SIMPLE</h1></div>

  <p class="intro">By offering a flat rate for our<br>tow services and by offering an<br>online payment solution where<br>you can get your vehicle towed<br>with just a few clicks of a<br>mouse, we lead the way in<br>being the most convenient tow<br>service in Houston.</p>

  <div class="website">www.tornilexautotransport.com</div>

  <svg class="guides" viewBox="0 0 879 1200" aria-hidden="true">
    <g fill="none" stroke="#fff" stroke-width="1.6">
      <path d="M245 11 V1030 C245 1050 230 1055 232 1070 C234 1085 250 1080 246 1096" stroke-dasharray="5 4"/>
      <circle cx="246" cy="733" r="130" stroke-dasharray="5 4"/>
      <path d="M376 733 V597" stroke-dasharray="5 4"/>
      <circle cx="411" cy="561" r="36"/>
      <path d="M421 537 c-8 -4 -14 2 -17 8 c-5 10 -4 24 2 34 c3 5 8 9 14 6 l3 -3 l-6 -9 l-4 2 c-4 -6 -5 -16 -2 -22 l4 1 l4 -11 z" stroke-width="2"/>
      <rect x="234" y="1098" width="25" height="42" rx="12" stroke-width="1.8"/>
      <path d="M234 1116 H259 M246.5 1098 V1116" stroke-width="1.8"/>
    </g>
  </svg>

  <p class="phone">(281) 555-0137</p>
  <p class="rate"><span class="rate-label">FLAT RATE TOWING</span><span class="rate-price">$75</span></p>
  <p class="email">service@tornilexautotransport.com</p>
</div>
</body>
</html>
```